Employee Benefits and Insurance Consulting

We are an existing company with over 30 years experience but are changing our name. We would like a simple design with grey tones.

Industry/Entity Type

Insurance

Contact Information for Business Card

Marlow Benefits Consulting
Gerald P Odell CEO
5172 Brackenfield Road
Louisville, TN 37777
gerald@marlowbx.com
865-412-3396 - O
865-247-5081 - C

```html
<!DOCTYPE html>
<html lang="en">
<head>
<meta charset="utf-8">
<title>Marlow Benefits Consulting – Business Card</title>
<link rel="stylesheet" href="https://fonts.googleapis.com/css2?family=Cabin:wght@400;600;700&display=swap">
<style>
  :root {
    --brand-grey: #45484c;
    --brand-grey-light: #8a8d91;
    --card-white: #ffffff;
    --ink-white: #ffffff;
    --rule-light: rgba(255, 255, 255, 0.26);
    --backdrop: #e9e8e6;
    --card-shadow: 0 6px 18px rgba(0, 0, 0, 0.18);
  }
  * { box-sizing: border-box; margin: 0; padding: 0; }
  html, body {
    width: 1200px;
    height: 900px;
    overflow: hidden;
  }
  body {
    position: relative;
    background: var(--backdrop);
    font-family: "Cabin", "Segoe UI", sans-serif;
  }

  .card {
    position: absolute;
    background: var(--card-white);
    box-shadow: var(--card-shadow);
    overflow: hidden;
  }

  /* Front card */
  .card--front {
    left: 77px;
    top: 34px;
    width: 588px;
    height: 363px;
  }
  .front-header {
    height: 139px;
    display: flex;
    align-items: center;
    padding-left: 33px;
    gap: 14px;
  }
  .brand-mark {
    width: 26px;
    height: 26px;
    background: var(--brand-grey-light);
    flex-shrink: 0;
  }
  .brand-name {
    font-size: 34px;
    font-weight: 700;
    color: var(--brand-grey);
    letter-spacing: 0.2px;
    white-space: nowrap;
  }
  .front-body {
    position: absolute;
    left: 0;
    top: 139px;
    width: 100%;
    height: 224px;
    background: var(--brand-grey);
    color: var(--ink-white);
  }
  .person {
    position: absolute;
    left: 32px;
    top: 14px;
    font-size: 21px;
    font-weight: 700;
  }
  .person .role {
    font-size: 15px;
    font-weight: 600;
  }
  .contact-list {
    list-style: none;
    position: absolute;
    left: 0;
    top: 56px;
    width: 248px;
  }
  .contact-list li {
    display: flex;
    align-items: center;
    gap: 10px;
    height: 37px;
    padding-left: 32px;
    font-size: 15px;
    border-top: 1px solid var(--rule-light);
    white-space: nowrap;
  }
  .contact-list li.address { height: 43px; }
  .contact-list svg { width: 12px; height: 12px; fill: var(--ink-white); flex-shrink: 0; }

  /* Back card */
  .card--back {
    left: 388px;
    top: 505px;
    width: 567px;
    height: 352px;
  }
  .back-band {
    position: absolute;
    left: 0;
    top: 110px;
    width: 100%;
    height: 131px;
    background: var(--brand-grey);
    display: flex;
    align-items: center;
    justify-content: center;
    gap: 14px;
  }
  .back-band .brand-mark { background: var(--ink-white); }
  .back-band .brand-name { color: var(--ink-white); font-size: 32px; }
</style>
</head>
<body>

  <section class="card card--front" aria-label="Business card front">
    <header class="front-header">
      <span class="brand-mark" aria-hidden="true"></span>
      <span class="brand-name">Marlow Benefits Consulting</span>
    </header>
    <div class="front-body">
      <p class="person">Gerald P Odell <span class="role">- CEO</span></p>
      <ul class="contact-list">
        <li class="address">5172 Brackenfield Road Louisville, TN 37777</li>
        <li class="office-phone">
          <svg viewBox="0 0 24 24" aria-label="Office"><path d="M6.6 10.8a15.1 15.1 0 0 0 6.6 6.6l2.2-2.2c.3-.3.7-.4 1-.2 1.1.4 2.3.6 3.6.6.6 0 1 .4 1 1V20c0 .6-.4 1-1 1C10.6 21 3 13.4 3 4c0-.6.4-1 1-1h3.5c.6 0 1 .4 1 1 0 1.3.2 2.5.6 3.6.1.3 0 .7-.2 1z"/></svg>
          865-412-3396
        </li>
        <li class="cell-phone">
          <svg viewBox="0 0 24 24" aria-label="Cell"><path d="M7 1h10a2 2 0 0 1 2 2v18a2 2 0 0 1-2 2H7a2 2 0 0 1-2-2V3a2 2 0 0 1 2-2zm0 3v14h10V4zm5 15.5a1 1 0 1 0 0 2 1 1 0 0 0 0-2z"/></svg>
          865-247-5081
        </li>
        <li class="email">
          <svg viewBox="0 0 24 24" aria-label="Email"><path d="M2 5h20v14H2zm2 2v.5l8 5 8-5V7zm0 2.8V17h16V9.8l-8 5z"/></svg>
          gerald@marlowbx.com
        </li>
      </ul>
    </div>
  </section>

  <section class="card card--back" aria-label="Business card back">
    <div class="back-band">
      <span class="brand-mark" aria-hidden="true"></span>
      <span class="brand-name">Marlow Benefits Consulting</span>
    </div>
  </section>

</body>
</html>
```